Halworth Builds, Carpentry Services

Business card for carpentry business in the Sunshine Coast.

Business card layout required using logo provided - provided both PDF copy and AI. Please let me know if you would like a the files for the logo symbol and text by itself.

Business Colours are grey, blue and white. The font colours codes for this design are Blue Hex # 00B4E6 and Hex # 39393B for the gray colour.

FYI font for logo is Gotham Bold.

Preference for a clean and striking layout that is simple and elegant.

Target Market(s)

Young Families, retirees, young couples requiring assistance with small to medium works/renovations on the Sunshine Coast.

Industry/Entity Type

Construction

Contact Information for Business Card

Dean Halworth
Carpenter
0481356027
dean@halworthbuilds.com.au
Kelvale Point, Sunrise Coast
RHLA Licensed Carpenter (In smaller font)

Font styles to use
Sans Serif

Colors

Designer to choose colors to be used in the design.

Requirements
Must have
• Logo provided must appear on the card, preferably on one side of the card by itself with the text on the alternate side
Nice to have
• Text on the other side of card, maybe grey background and white font here but happy for the designer to provide ideas here.
Should not have
• Use of other colours, other than the ones provided - white, grey and blue. Black optional.

```html
<!DOCTYPE html>
<html lang="en">
<head>
<meta charset="UTF-8">
<title>Halworth Builds – Business Card</title>
<link rel="stylesheet" href="https://fonts.googleapis.com/css2?family=Montserrat:wght@500;600;700&display=swap">
<style>
  :root {
    --blue: #00B4E6;
    --grey: #39393B;
    --white: #F7F7F7;
    --stage: #E6E3DE;
  }
  * { margin: 0; padding: 0; box-sizing: border-box; }
  html, body {
    width: 900px; height: 1200px; overflow: hidden;
    background: var(--stage);
    font-family: "Montserrat", Arial, sans-serif;
  }
  .canvas { position: relative; width: 900px; height: 1200px; }

  .card {
    position: absolute; left: 75px; width: 768px;
    border-radius: 20px;
  }
  .card--front { top: 133px; height: 438px; background: var(--white); }
  .card--back  { top: 628px; height: 444px; background: var(--grey); }

  .brand-name {
    position: absolute; left: 0; right: 0;
    text-align: center;
    font-weight: 700;
    color: var(--blue);
    letter-spacing: 0.5px;
  }
  .card--front .brand-name { top: 110px; font-size: 46px; }
  .card--back .brand-name  { top: 188px; font-size: 58px; }

  .person { position: absolute; left: 53px; top: 251px; color: var(--grey); }
  .person__name { font-size: 21px; font-weight: 700; letter-spacing: 0.3px; }
  .person__name .accent { color: var(--blue); }
  .person__role { font-size: 19px; font-weight: 500; margin-top: 2px; }

  .contact { position: absolute; left: 335px; top: 246px; list-style: none; color: var(--grey); }
  .contact li {
    display: flex; align-items: center;
    font-size: 20px; font-weight: 500; height: 29px;
  }
  .contact svg { width: 17px; height: 17px; margin-right: 12px; fill: var(--blue); flex: none; }

  .licence {
    position: absolute; left: 53px; right: 52px; top: 387px;
    display: flex; align-items: center; gap: 10px;
    font-size: 17.5px; font-weight: 500; color: var(--grey);
  }
  .licence::before, .licence::after {
    content: ""; flex: 1; height: 2px; background: var(--blue);
  }
</style>
</head>
<body>
<main class="canvas">
  <section class="card card--front">
    <div class="brand-name">Halworth Builds</div>

    <div class="person">
      <div class="person__name">DEAN <span class="accent">HALWORTH</span></div>
      <div class="person__role">Carpenter</div>
    </div>

    <ul class="contact">
      <li>
        <svg viewBox="0 0 24 24" aria-hidden="true"><path d="M6.6 10.8a15.1 15.1 0 0 0 6.6 6.6l2.2-2.2a1 1 0 0 1 1-.25 11.4 11.4 0 0 0 3.6.57 1 1 0 0 1 1 1V20a1 1 0 0 1-1 1A17 17 0 0 1 3 4a1 1 0 0 1 1-1h3.5a1 1 0 0 1 1 1c0 1.25.2 2.45.57 3.57a1 1 0 0 1-.25 1z"/></svg>
        04 81 35 60 27
      </li>
      <li>
        <svg viewBox="0 0 24 24" aria-hidden="true"><path d="M2 5h20v2l-10 6L2 7z M2 9.3l10 6 10-6V19H2z"/></svg>
        dean@halworthbuilds.com.au
      </li>
      <li>
        <svg viewBox="0 0 24 24" aria-hidden="true"><path d="M12 1.5a7.5 7.5 0 0 0-7.5 7.5c0 5.6 7.5 13.5 7.5 13.5s7.5-7.9 7.5-13.5A7.5 7.5 0 0 0 12 1.5zm0 10.3a2.8 2.8 0 1 1 0-5.6 2.8 2.8 0 0 1 0 5.6z"/></svg>
        Kelvale Point, Sunrise Coast
      </li>
    </ul>

    <div class="licence">RHLA Licensed Carpenter</div>
  </section>

  <section class="card card--back">
    <div class="brand-name">Halworth Builds</div>
  </section>
</main>
</body>
</html>
```